Business Card and Letterhead for new company Vardel GreenWorks, Inc.

Vardel GreenWorks, Inc., an engineering and construction firm that provides services for solid waste landfill gas systems, needs a business card and letterhead. We recently had a logo designed but we are open to some tweaks to logo design and color scheme. Generally, we like "earthy" color tones - greens, browns, oranges. This is a sister company - www.talvoriengineering.example.

Target Market(s)

Solid waste landfill companies - Brindle Disposal, Halcott Hauling, etc.

Industry/Entity Type

Engineering and Construction

Contact Information for Business Card

Name, Title, email, mobile phone, work phone, website. Potential list of services for back of card: LFG Engineering and Design, GCCS Planning and Operational Consulting, Compliance Monitoring and Reporting, Routine Operations & Maintenance, Nonroutine O&M, Construction Management, Construction QA, GCCS Construction

Font styles to use
Sans Serif

Requirements
Must have
• Logo, pertinent information, maybe a tagline (still in development)
Nice to have
• For back of card, considering an engineering scale (attached for another business of ours), but want to look at other options, alternatives. Like the idea of the back of card to have some utility (scale, unit conversion info, list of services) but willing to consider lots of options.
Should not have
• Needs to have a professional (engineering) and technical look, not cartoonish.

```html
<!DOCTYPE html>
<html lang="en">
<head>
<meta charset="utf-8">
<title>Vardel GreenWorks — Stationery</title>
<link href="https://fonts.googleapis.com/css2?family=Work+Sans:wght@400;500;600;700&display=swap" rel="stylesheet">
<style>
  :root {
    --backdrop: #b5b5b5;
    --paper: #ffffff;
    --brand-green: #74b32f;
    --ink-grey: #6f6f6f;
    --ink-dark: #5a5a5a;
    --rule: #9a9a9a;
    --shadow: 4px 6px 10px rgba(0,0,0,0.28);
  }
  * { box-sizing: border-box; margin: 0; padding: 0; }
  html, body { width: 1200px; height: 1000px; overflow: hidden; }
  body {
    background: var(--backdrop);
    font-family: "Work Sans", Arial, sans-serif;
    position: relative;
  }
  .sheet, .card { position: absolute; background: var(--paper); box-shadow: var(--shadow); }

  .letterhead { left: 75px; top: 150px; width: 506px; height: 696px; }
  .card-front { left: 618px; top: 355px; width: 400px; height: 229px; background: var(--brand-green); }
  .card-back { left: 618px; top: 616px; width: 400px; height: 229px; }

  .wordmark {
    position: absolute;
    display: flex; align-items: center; gap: 7px;
    font-weight: 700; color: var(--ink-grey);
    letter-spacing: 0.3px; white-space: nowrap;
  }
  .wordmark .dot { width: 14px; height: 14px; border-radius: 50%; background: var(--brand-green); }
  .letterhead .wordmark { left: 24px; top: 44px; font-size: 17px; }
  .card-back .wordmark { left: 24px; top: 36px; font-size: 17px; }
  .card-front .wordmark {
    left: 0; right: 0; top: 100px; justify-content: center;
    font-size: 20px; color: #ffffff;
  }
  .card-front .wordmark .dot { background: #ffffff; width: 16px; height: 16px; }

  .contact-line { list-style: none; font-size: 11px; color: var(--ink-grey); }
  .contact-line li { display: flex; align-items: center; gap: 4px; }
  .contact-line svg { width: 8px; height: 8px; fill: var(--brand-green); flex: none; }

  .letterhead-footer {
    position: absolute; left: 56px; bottom: 13px;
    display: flex; gap: 8px;
  }

  .employee { position: absolute; left: 21px; top: 120px; }
  .employee-name { font-size: 11.5px; font-weight: 700; color: var(--brand-green); }
  .employee-title {
    font-size: 11.5px; color: var(--ink-grey);
    width: 95px; padding-bottom: 2px; border-bottom: 1px solid var(--rule);
  }
  .card-contacts { position: absolute; left: 21px; top: 168px; }
  .card-contacts.contact-line { font-size: 9.5px; line-height: 12px; }

  .services {
    position: absolute; right: 16px; top: 120px;
    list-style: none; text-align: right;
    font-size: 9px; font-weight: 600; color: var(--ink-dark); line-height: 12px;
  }
  .services li::after { content: " •"; color: var(--brand-green); }
</style>
</head>
<body>

<section class="sheet letterhead" aria-label="Letterhead">
  <div class="wordmark"><span class="dot"></span>Vardel GreenWorks</div>
  <ul class="contact-line letterhead-footer">
    <li><svg viewBox="0 0 10 10"><path d="M2 0h2l1 3-1.5 1a6 6 0 0 0 2.5 2.5L7 5l3 1v2a2 2 0 0 1-2 2A8 8 0 0 1 0 2a2 2 0 0 1 2-2z"/></svg>office phone</li>
    <li><svg viewBox="0 0 10 10"><path d="M0 2h10v6H0zM0 2l5 3 5-3" /></svg>email@vardelgreenworks.example</li>
    <li><svg viewBox="0 0 10 10"><circle cx="5" cy="5" r="5"/></svg>vardelgreenworks.example</li>
  </ul>
</section>

<section class="card card-front" aria-label="Business card front">
  <div class="wordmark"><span class="dot"></span>Vardel GreenWorks</div>
</section>

<section class="card card-back" aria-label="Business card back">
  <div class="wordmark"><span class="dot"></span>Vardel GreenWorks</div>
  <div class="employee">
    <p class="employee-name">Employee Name</p>
    <p class="employee-title">Title</p>
  </div>
  <ul class="contact-line card-contacts">
    <li><svg viewBox="0 0 10 10"><path d="M2 0h6v10H2zM3 1v7h4V1z"/></svg>mobile phone</li>
    <li><svg viewBox="0 0 10 10"><path d="M2 0h2l1 3-1.5 1a6 6 0 0 0 2.5 2.5L7 5l3 1v2a2 2 0 0 1-2 2A8 8 0 0 1 0 2a2 2 0 0 1 2-2z"/></svg>office phone</li>
    <li><svg viewBox="0 0 10 10"><path d="M0 2h10v6H0z"/></svg>email@vardelgreenworks.example</li>
    <li><svg viewBox="0 0 10 10"><circle cx="5" cy="5" r="5"/></svg>vardelgreenworks.example</li>
  </ul>
  <ul class="services">
    <li>LFG Engineering and Design</li>
    <li>GCCS Planning and Operational Consulting</li>
    <li>Compliance Monitoring and Reporting</li>
    <li>Routine Operations &amp; Maintenance</li>
    <li>Nonroutine O&amp;M</li>
    <li>Construction Management</li>
    <li>Construction QA</li>
    <li>GCCS Construction</li>
  </ul>
</section>

</body>
</html>
```